Designing business cards for my start-up business

The company is called Pellion. We are a start-up tech data company based in Guernsey, Channel Islands. We want the business cards to look clean, fresh and innovative, just what a tech company should be. We do not want the business cards to look corporate or too official such as a bank. I would like the front of the business card to have our logo and the tag line of "connecting talent". On the back will be our contact details, emails etc. However I am open to your ideas and suggestions. I have provided all our logos and a word doc of all our contact details. There are 4 directors of the business, so I want 4 versions of the same design.

Target Market(s)

Our clients are businesses of all industries. Its a broad target market.

Industry/Entity Type

Information Technology

Contact Information for Business Card

I have attached a word doc called "Business Cards info" which gives all contact details of the 4 employees for the company.

Requirements
Must have
• We must have our logo and the tag line of "connecting talent". This could on the front of the card and then the individuals contact details on the back. Other than that, I'm happy for the designers to come up with ideas/styles.
Nice to have
• N/A
Should not have
• I don't want the cards to look too formal or corporate. As mentioned, we are a tech start-up so we want to look innovative.

```html
<!DOCTYPE html>
<html lang="en">
<head>
<meta charset="utf-8">
<title>Pellion business cards</title>
<link href="https://fonts.googleapis.com/css2?family=Open+Sans:wght@400;700&family=Arimo:wght@400&display=swap" rel="stylesheet">
<style>
  :root {
    --backdrop: #1f1f1f;
    --card-face: #efefef;
    --band-grey: #c8c8c8;
    --accent: #e4533a;
    --ink: #1a1a1a;
    --muted: #555555;
    --white: #ffffff;
  }
  * { margin: 0; padding: 0; box-sizing: border-box; }
  html, body { width: 1200px; height: 800px; overflow: hidden; }
  body { background: var(--backdrop); position: relative; }

  .card {
    position: absolute;
    top: 238px;
    width: 670px;
    height: 382px;
    background: var(--card-face);
    transform: scale(0.8);
    transform-origin: top left;
    overflow: hidden;
  }
  .card--details { left: 49px; }
  .card--brand { left: 617px; }

  .card__bands { position: absolute; inset: 0; width: 670px; height: 382px; }
  .band--grey { fill: var(--band-grey); }
  .band--accent { fill: var(--accent); }

  .holder-name {
    position: absolute; left: 35px; top: 128px;
    font: 400 30px/1 "Open Sans", sans-serif;
    color: var(--accent);
  }
  .holder-role {
    position: absolute; left: 35px; top: 163px;
    font: 400 17px/1.2 "Open Sans", sans-serif;
    color: var(--ink);
  }
  .address {
    position: absolute; left: 35px; top: 200px;
    font: 400 17px/25px "Arimo", sans-serif;
    color: var(--ink);
  }
  .contact-list {
    position: absolute; left: 38px; top: 270px;
    list-style: none;
    font: 400 17px/23px "Arimo", sans-serif;
    color: var(--ink);
  }
  .contact-list li { display: flex; align-items: center; gap: 13px; height: 23px; }
  .contact-icon { width: 17px; height: 17px; flex: none; }
  .contact-icon rect { fill: var(--accent); }
  .contact-icon .glyph { fill: none; stroke: var(--white); stroke-width: 1.4; }

  .brand-mark {
    position: absolute;
    background: var(--accent);
  }
  .brand-name {
    position: absolute;
    font-family: "Open Sans", sans-serif;
    font-weight: 700;
    color: var(--ink);
    text-align: center;
  }
  .tagline {
    position: absolute;
    font: 400 16px/1 "Open Sans", sans-serif;
    letter-spacing: 4px;
    color: var(--muted);
    text-align: center;
    text-transform: lowercase;
  }
  .card--details .brand-mark { left: 453px; top: 40px; width: 174px; height: 170px; }
  .card--details .brand-name { left: 440px; top: 228px; width: 200px; font-size: 27px; letter-spacing: 9px; line-height: 1; }
  .card--brand .brand-mark { left: 236px; top: 42px; width: 200px; height: 194px; }
  .card--brand .brand-name { left: 200px; top: 254px; width: 272px; font-size: 35px; letter-spacing: 12px; line-height: 1; }
  .card--brand .tagline { left: 186px; top: 306px; width: 300px; }
</style>
</head>
<body>

  <section class="card card--details" aria-label="Card back with contact details">
    <svg class="card__bands" viewBox="0 0 670 382" aria-hidden="true">
      <path class="band--grey" d="M0,0 H670 V22 H300 C240,22 230,107 165,107 H0 Z"/>
      <path class="band--accent" d="M670,382 H0 V364 H420 C485,364 490,272 560,272 H670 Z"/>
    </svg>

    <h1 class="holder-name">Marcus Hale</h1>
    <p class="holder-role">Director</p>
    <p class="address">17 Rue Verte, St Sampson, Guernsey,<br>GY2 4XL, Channel Islands</p>

    <ul class="contact-list">
      <li>
        <svg class="contact-icon" viewBox="0 0 17 17" aria-hidden="true">
          <rect width="17" height="17"/>
          <rect class="glyph" x="5.5" y="3" width="6" height="11" rx="1"/>
        </svg>
        +447700900412
      </li>
      <li>
        <svg class="contact-icon" viewBox="0 0 17 17" aria-hidden="true">
          <rect width="17" height="17"/>
          <path class="glyph" d="M3.5,5 H13.5 V12 H3.5 Z M3.5,5 L8.5,9 L13.5,5"/>
        </svg>
        Marcus.Hale@pellion.gg
      </li>
      <li>
        <svg class="contact-icon" viewBox="0 0 17 17" aria-hidden="true">
          <rect width="17" height="17"/>
          <circle class="glyph" cx="8.5" cy="8.5" r="5"/>
          <path class="glyph" d="M3.5,8.5 H13.5 M8.5,3.5 C6,6 6,11 8.5,13.5 C11,11 11,6 8.5,3.5"/>
        </svg>
        www.pellion.gg
      </li>
    </ul>

    <div class="brand-mark" aria-hidden="true"></div>
    <p class="brand-name">Pellion</p>
  </section>

  <section class="card card--brand" aria-label="Card front with company name and tagline">
    <svg class="card__bands" viewBox="0 0 670 382" aria-hidden="true">
      <path class="band--accent" d="M0,0 H670 V22 H240 C185,22 175,107 105,107 H0 Z"/>
      <path class="band--grey" d="M670,382 H0 V364 H420 C485,364 490,272 560,272 H670 Z"/>
    </svg>

    <div class="brand-mark" aria-hidden="true"></div>
    <p class="brand-name">Pellion</p>
    <p class="tagline">connecting talent</p>
  </section>

</body>
</html>
```